Shop TalkWave w/Morna Pell (podcast)

Podcast graphic to attract listeners interested in small business tax, bookkeeping and payroll issues. Shop TalkWave w/Morna Pell. Simple, clever and clear. Bold colors that attract attention and make small business owners interested in listening to her and wanting to get to know her. We want to her to appear to be a coach and expert on small business.

Target Market(s)

women and men in small business

Industry/Entity Type

Business Consultant

Font styles to use
Sans Serif

Colors
b260a6
f78f20
32a6d7

Requirements
Must have
• Warm and inviting, positive and uplifting. Promote a personable lady ready and willing to loyally serve her clients and help them succeed in business.
Nice to have
• Clever and smart attracting people that want her business service and advice.
• Emphasize her warmness and open personality.
Should not have
• Nasty or inappropriate,

```html
<!DOCTYPE html>
<html lang="en">
<head>
<meta charset="utf-8">
<title>Shop TalkWave w/Morna Pell</title>
<link rel="stylesheet" href="https://fonts.googleapis.com/css2?family=Lilita+One&display=swap">
<style>
  :root {
    --orange: #f78f20;
    --purple: #b260a6;
    --blue: #32a6d7;
    --white: #ffffff;
    --navy: #0d4468;
    --hair: #1c1416;
  }
  html, body {
    margin: 0;
    padding: 0;
    width: 1200px;
    height: 794px;
    overflow: hidden;
    background: var(--purple);
  }
  .poster {
    display: block;
    width: 1200px;
    height: 794px;
  }
  .headline {
    font-family: "Lilita One", "Arial Black", sans-serif;
    paint-order: stroke fill;
    stroke: var(--white);
    stroke-linejoin: round;
  }
  .show-title { fill: var(--orange); stroke-width: 7px; }
  .connector { fill: var(--blue); stroke-width: 4px; }
  .host-name { fill: var(--purple); stroke-width: 7px; }
  .network-name {
    font-family: "Lilita One", "Arial Black", sans-serif;
    fill: var(--white);
  }
  .network-dot { fill: var(--white); }
</style>
</head>
<body>
<svg class="poster" viewBox="0 0 1200 794" xmlns="http://www.w3.org/2000/svg">
  <defs>
    <linearGradient id="hostTone" x1="0" y1="0" x2="0" y2="1">
      <stop offset="0" stop-color="#2a1c1e"/>
      <stop offset="0.45" stop-color="#c98f7c"/>
      <stop offset="0.65" stop-color="#f29a2a"/>
      <stop offset="1" stop-color="#f6a233"/>
    </linearGradient>
  </defs>

  <rect class="bg-purple" width="1200" height="794" fill="var(--purple)"/>
  <polygon class="bg-orange" points="0,0 720,0 466,794 0,794" fill="var(--orange)"/>

  <g transform="rotate(-4 400 400)">
    <text class="headline show-title" x="36" y="232" font-size="150" textLength="720" lengthAdjust="spacingAndGlyphs">"Shop TalkWave</text>
    <text class="headline connector" x="182" y="420" font-size="118" textLength="222" lengthAdjust="spacingAndGlyphs">With</text>
    <text class="headline host-name" x="58" y="676" font-size="160" textLength="628" lengthAdjust="spacingAndGlyphs">Morna Pell"</text>
  </g>

  <g class="network">
    <circle class="network-dot" cx="528" cy="398" r="9"/>
    <text class="network-name" x="544" y="407" font-size="24">Brightline Podcast</text>
  </g>

  <path class="host-photo" role="img" aria-label="Portrait photo of the host, smiling over her shoulder in an orange top"
        d="M955 120 C1040 125 1105 190 1115 280 C1125 360 1112 430 1122 510 C1132 590 1150 680 1160 794 L655 794 C690 720 760 640 860 560 C850 520 845 470 830 430 C805 400 800 320 810 260 C825 180 885 118 955 120 Z"
        fill="url(#hostTone)" stroke="var(--white)" stroke-width="3"/>
</svg>
</body>
</html>
```